Business Card for a mobile physiotherapy company

I need a layout for a business card for a mobile physiotherapy company.
Slogan is "Mobile Physiotherapy - Your Road To Recovery"
Phone number is 867-412-5093
Email VantePhysio@mailbox-demo.ca (subject to change with website)
Website www.VantePhysio.ca
My name and credentials: Gil Varney Gil Varney, BSc(kin), MPT, CAFCI, IMS
Information maybe included: Direct Billing, Services including Physiotherapy, IMS, acupuncture
Maybe include facebook and instagram logos
One side with the logo clean and sharp
Other side with details, try not to look too busy, keep everything concise

```html
<!DOCTYPE html>
<html lang="en">
<head>
<meta charset="utf-8">
<title>Vante Therapy – Business Card</title>
<link rel="stylesheet" href="https://fonts.googleapis.com/css2?family=Tinos:wght@700&family=Lato:wght@400&display=swap">
<style>
  :root {
    --stage: #2a2a2a;
    --paper: #ffffff;
    --pine: #0d5a45;
    --navy: #2b4a7e;
    --ink: #1c1c1c;
    --rule: #9aa3b5;
    --teal-deep: #0f5a4c;
    --navy-deep: #2a4872;
    --white: #ffffff;
  }
  * { box-sizing: border-box; margin: 0; padding: 0; }
  html, body { width: 1200px; height: 900px; overflow: hidden; background: var(--stage); }
  .canvas { position: relative; width: 1200px; height: 900px; }

  .card {
    position: absolute; top: 200px; width: 310px; height: 502px;
    box-shadow: 4px 5px 6px rgba(0,0,0,0.55);
    text-align: center;
  }
  .card--details {
    left: 253px; background: var(--paper);
    border-radius: 66px 0 66px 0;
  }
  .card--brand {
    left: 627px;
    border-radius: 0 66px 0 66px;
    background: linear-gradient(200deg, var(--navy-deep) 0%, #1f5466 50%, var(--teal-deep) 100%);
    color: var(--white);
  }

  .serif { font-family: "Tinos", "Times New Roman", serif; font-weight: 700; }
  .sans { font-family: "Lato", Arial, sans-serif; font-weight: 400; }

  .brand-mark { position: absolute; left: 0; right: 0; }
  .brand-mark__dot {
    display: block; width: 44px; height: 44px; margin: 0 auto 14px;
    border-radius: 50%; background: var(--pine);
  }
  .brand-mark__name { display: block; color: var(--pine); line-height: 1; }
  .card--details .brand-mark { top: 88px; }
  .card--details .brand-mark__primary { font-size: 44px; letter-spacing: 4px; }
  .card--details .brand-mark__secondary { font-size: 19px; letter-spacing: 6.5px; margin-top: 10px; }

  .holder { position: absolute; top: 260px; left: 0; right: 0; }
  .holder__name { color: var(--pine); font-size: 20px; letter-spacing: 0.5px; line-height: 1.1; }
  .holder__creds { color: var(--navy); font-size: 14px; margin-top: 3px; }

  .divider-icons {
    position: absolute; top: 312px; left: 74px; width: 162px; height: 20px;
    display: flex; align-items: center; gap: 4px;
  }
  .divider-icons__line { flex: 1; height: 1px; background: var(--rule); }
  .divider-icons svg { width: 18px; height: 18px; display: block; }

  .contact { position: absolute; top: 342px; left: 0; right: 0; color: var(--ink); font-size: 14px; line-height: 18.5px; }
  .contact__rule { position: absolute; top: 405px; left: 72px; width: 166px; height: 1px; background: var(--rule); }
  .services { position: absolute; top: 416px; left: 0; right: 0; color: var(--navy); font-size: 14.5px; line-height: 18px; }

  .card--brand .brand-mark { top: 287px; }
  .card--brand .brand-mark__name { color: var(--white); }
  .card--brand .brand-mark__primary { font-size: 52px; letter-spacing: 6px; margin-left: 6px; }
  .card--brand .brand-mark__secondary { font-size: 23px; letter-spacing: 8px; margin-top: 8px; margin-left: 8px; }

  .slogan { position: absolute; top: 392px; left: 0; right: 0; font-size: 14.5px; line-height: 18px; letter-spacing: 0.2px; }

  .social { position: absolute; top: 443px; left: 54px; width: 204px; height: 22px; display: flex; align-items: center; gap: 5px; }
  .social__line { flex: 1; height: 1px; background: rgba(255,255,255,0.45); }
  .social__dot { width: 21px; height: 21px; border-radius: 50%; background: var(--white); }
</style>
</head>
<body>
<main class="canvas">

  <section class="card card--details" aria-label="Card back with contact details">
    <div class="brand-mark">
      <span class="brand-mark__dot"></span>
      <span class="brand-mark__name brand-mark__primary serif">VANTE</span>
      <span class="brand-mark__name brand-mark__secondary serif">THERAPY</span>
    </div>

    <div class="holder">
      <p class="holder__name serif">GIL VARNEY</p>
      <p class="holder__creds sans">BSC(KIN), MPT, CAFCI, IMS</p>
    </div>

    <div class="divider-icons">
      <span class="divider-icons__line"></span>
      <svg viewBox="0 0 20 20" aria-label="Phone"><circle cx="10" cy="10" r="10" fill="#0d5a45"/><path d="M5 8.5c0-1.5 2.3-2.5 5-2.5s5 1 5 2.5l-1.6.8-1-1.3H7.6l-1 1.3z M7 10h6l1 4H6z" fill="#fff"/></svg>
      <svg viewBox="0 0 20 20" aria-label="Email"><circle cx="10" cy="10" r="10" fill="#0d5a45"/><rect x="5" y="6.5" width="10" height="7" fill="#fff"/><path d="M5 6.5l5 4 5-4" fill="none" stroke="#0d5a45" stroke-width="1"/></svg>
      <svg viewBox="0 0 20 20" aria-label="Website"><circle cx="10" cy="10" r="10" fill="#0d5a45"/><circle cx="10" cy="10" r="5" fill="none" stroke="#fff" stroke-width="1.3"/><path d="M5 10h10M10 5c-2.5 3-2.5 7 0 10M10 5c2.5 3 2.5 7 0 10" fill="none" stroke="#fff" stroke-width="1"/></svg>
      <span class="divider-icons__line"></span>
    </div>

    <address class="contact sans" style="font-style: normal;">
      <p>867-412-5093</p>
      <p>VantePhysio@mailbox-demo.ca</p>
      <p>www.VantePhysio.ca</p>
    </address>
    <span class="contact__rule"></span>

    <ul class="services sans" style="list-style: none;">
      <li>Direct Billing</li>
      <li>Service Including Physiotherapy</li>
      <li>IMS | acupuncture</li>
    </ul>
  </section>

  <section class="card card--brand" aria-label="Card front with brand name">
    <div class="brand-mark">
      <span class="brand-mark__name brand-mark__primary serif">VANTE</span>
      <span class="brand-mark__name brand-mark__secondary serif">THERAPY</span>
    </div>

    <p class="slogan sans">MOBILE PHYSIOTHERAPY<br>YOUR ROAD TO RECOVERY</p>

    <div class="social" aria-label="Social profiles">
      <span class="social__line"></span>
      <span class="social__dot"></span>
      <span class="social__dot"></span>
      <span class="social__line"></span>
    </div>
  </section>

</main>
</body>
</html>
```